Hand sanitizer logos and bottle design

Want a very simple and clean logo for - PURA42.
Need a badge logo for - Clean Shield 42 Keeper.
Need bottle label designed. Mock up is attached. Keep it very clean as in mockup.
Target Market(s)
retail
Font styles to use
Sans Serif
Requirements
Must have
- Simple Clean

```html
<!DOCTYPE html>
<html lang="en">
<head>
<meta charset="utf-8">
<title>PURA42 Gel Hand Sanitizer Label</title>
<link href="https://fonts.googleapis.com/css2?family=Montserrat:wght@500;600;700;800&family=Saira+Semi+Condensed:wght@700&display=swap" rel="stylesheet">
<style>
  :root {
    --backdrop: #b8b8b8;
    --label-white: #f2f2f2;
    --brand-orange: #e46a0c;
    --ink-dark: #4a4a4a;
    --ink-text: #3a3a3a;
    --shield-blue: #1e7fe3;
    --paper: #ffffff;
    --clock-grey: #d6d6d6;
    --clock-grey-soft: #e6e6e6;
  }
  * { margin: 0; padding: 0; box-sizing: border-box; }
  html, body {
    width: 1200px; height: 800px; overflow: hidden;
    background: var(--backdrop);
    font-family: "Montserrat", sans-serif;
  }
  .label {
    position: absolute; left: 340px; top: 50px;
    width: 520px; height: 700px;
    background: linear-gradient(90deg, #f7f7f7 0%, var(--label-white) 100%);
    border-radius: 14px;
    overflow: hidden;
  }
  .brand-name {
    position: absolute; left: 18px; top: 560px;
    transform: rotate(-90deg); transform-origin: left top;
    font-weight: 800; font-size: 112px; line-height: 1;
    color: var(--brand-orange); letter-spacing: -2px;
    white-space: nowrap;
  }
  .product-tag {
    position: absolute; left: 170px; top: 122px;
    background: var(--brand-orange); color: var(--paper);
    font-weight: 600; font-size: 25px; letter-spacing: -0.5px;
    padding: 2px 14px; line-height: 32px;
  }
  .claim {
    position: absolute; left: 170px; top: 185px;
    font-weight: 700; font-size: 34px; line-height: 36px;
    color: var(--ink-dark);
  }
  .claim-details {
    position: absolute; left: 170px; top: 274px;
    font-weight: 500; font-size: 13px; line-height: 16px;
    color: var(--ink-text);
  }
  .keeper-badge {
    position: absolute; left: 382px; top: 190px;
    width: 110px; text-align: center;
  }
  .keeper-badge .dot {
    width: 36px; height: 36px; border-radius: 50%;
    background: var(--shield-blue); margin: 0 auto 8px;
  }
  .keeper-badge .badge-name {
    font-weight: 700; font-size: 15px; line-height: 17px;
    color: var(--shield-blue); text-transform: uppercase;
  }
  .duration {
    position: absolute; left: 240px; top: 330px;
    width: 200px; height: 110px;
  }
  .duration .hours {
    position: absolute; left: 0; top: 6px;
    font-weight: 600; font-size: 66px; line-height: 66px;
    color: var(--brand-orange);
  }
  .duration .clock-art {
    position: absolute; left: 84px; top: 0;
    width: 100px; height: 100px; border-radius: 12px;
    background: linear-gradient(135deg, var(--clock-grey-soft) 0%, var(--clock-grey) 100%);
  }
  .protection {
    position: absolute; left: 246px; top: 446px;
    font-family: "Saira Semi Condensed", sans-serif;
    font-weight: 700; font-size: 38px; line-height: 44px;
    color: var(--ink-dark); transform: skewX(-10deg);
    white-space: nowrap;
  }
  .benefit {
    position: absolute; left: 170px; top: 518px; width: 320px;
    text-align: center; font-weight: 500; font-size: 14px; line-height: 22px;
    color: var(--ink-text);
  }
  .volume-band {
    position: absolute; left: 0; top: 602px; width: 520px; height: 56px;
    background: var(--brand-orange); color: var(--paper);
    display: flex; align-items: center; justify-content: center; gap: 12px;
  }
  .volume-band .net {
    font-weight: 600; font-size: 9px; line-height: 11px;
  }
  .volume-band .net span { font-size: 13px; display: block; }
  .volume-band .amount { font-weight: 600; font-size: 14px; }
</style>
</head>
<body>
  <main class="label">
    <div class="brand-name">PURA42</div>

    <div class="product-tag">GEL HAND SANITIZER</div>

    <h1 class="claim">KILLS 90%<br>OF GERMS</h1>
    <p class="claim-details">ALCHOHOL&nbsp; FREE<br>EXTENTED PROTECTION</p>

    <div class="keeper-badge">
      <div class="dot"></div>
      <div class="badge-name">Clean Shield 42 Keeper</div>
    </div>

    <div class="duration">
      <div class="hours">12</div>
      <div class="clock-art" role="img" aria-label="Clock dial illustration with a tick mark showing 12-hour protection"></div>
    </div>

    <div class="protection">PROTECTION</div>

    <p class="benefit">NANOTHECHNOLOGY ENABLE ONE USE<br>THAT WILL NOT DRY YOUR SKIN</p>

    <div class="volume-band">
      <div class="net">CONT.<span>NET</span></div>
      <div class="amount">500ML</div>
    </div>
  </main>
</body>
</html>
```